Wordpress Design Project

We are a Computer / Information Technology Company that will focus on the after-hours technical support for Home and Businesses.

I'm looking to have the home page as a static page with a links to blog, about us.

www.qmvolt.com.au is my web site.

Please do not chage uploaded logo's, do not copy current logo on website use uploaded files only, thanks.
Updates

Cheers

Derek

Target Market(s)

Home and Small office/home office, or SOHO Computer users.

Industry/Entity Type

Computer

Requirements
Should not have
• After hours tech support added to logo.

```html
<!DOCTYPE html>
<html lang="en">
<head>
<meta charset="utf-8">
<title>QM Volt – Technology in your hands</title>
<link rel="stylesheet" href="https://fonts.googleapis.com/css2?family=Noto+Sans:wght@400;700&family=Arimo:ital@0;1&display=swap">
<style>
  :root {
    --header-bg: #363636;
    --nav-bg: #3a3a3a;
    --accent: #00b2f0;
    --brand: #1d8fe0;
    --white: #ffffff;
    --ink: #111111;
    --night: #000000;
    --muted: #9a9a9a;
  }
  * { margin: 0; padding: 0; box-sizing: border-box; }
  html, body { width: 800px; height: 1200px; overflow: hidden; }
  body { position: relative; background: var(--white); font-family: "Noto Sans", sans-serif; color: var(--ink); }
  .abs { position: absolute; }

  .site-header { left: 0; top: 0; width: 800px; height: 152px; background: var(--header-bg); }
  .brand { left: 14px; top: 66px; display: flex; align-items: center; gap: 14px; }
  .brand-dot { width: 60px; height: 60px; border-radius: 50%; background: #8a8a8a; }
  .brand-name { font-size: 38px; font-weight: 700; color: var(--brand); letter-spacing: 1px; }
  .login-field { top: 94px; width: 79px; height: 18px; background: var(--white); border-radius: 4px; font-size: 8px; line-height: 18px; text-align: center; color: #222; }
  .login-links { left: 608px; top: 122px; font-size: 12px; color: var(--white); word-spacing: 2px; }

  .hero { left: 0; top: 152px; width: 800px; height: 339px;
    background:
      radial-gradient(ellipse 220px 120px at 36% 38%, rgba(110,210,230,.55), rgba(110,210,230,0) 70%),
      radial-gradient(ellipse 140px 60px at 42% 52%, rgba(90,120,255,.45), rgba(90,120,255,0) 70%),
      radial-gradient(ellipse 120px 50px at 14% 85%, rgba(255,170,60,.35), rgba(255,170,60,0) 70%),
      linear-gradient(160deg, #1f3a42 0%, #16262c 40%, #101619 75%, #0b0e10 100%); }
  .hero-line { font-family: "Arimo", sans-serif; font-style: italic; color: var(--white); }
  .hero-title { right: 16px; top: 240px; font-size: 38px; }
  .hero-sub { right: 32px; top: 290px; font-size: 27px; }

  .main-nav { left: 0; top: 491px; width: 800px; height: 45px; background: var(--nav-bg); font-family: "Arimo", sans-serif; }
  .nav-item { top: 0; line-height: 45px; font-size: 12.5px; color: var(--white); }
  .nav-home { left: 24px; top: 9px; width: 89px; height: 31px; border-radius: 3px; background: var(--accent); line-height: 31px; text-align: center; }
  .search-box { left: 632px; top: 14px; width: 120px; height: 17px; border-radius: 5px; background: var(--white); }
  .search-icon { left: 758px; top: 13px; }

  .feature-title { top: 566px; font-size: 20px; font-weight: 400; text-align: center; color: var(--ink); }
  .copy { font-size: 9.3px; line-height: 11.6px; text-align: justify; letter-spacing: -0.1px; }
  .features .copy { top: 756px; color: var(--ink); }
  .read-more { top: 898px; width: 51px; height: 25px; border-radius: 6px; background: var(--accent); color: var(--white); font-size: 7.5px; font-weight: 700; line-height: 25px; text-align: center; }

  .lower { left: 0; top: 942px; width: 800px; height: 258px; background: var(--night); }
  .lower-title { top: 958px; font-size: 20px; font-weight: 400; color: var(--white); }
  .lower-copy { color: var(--white); }
  .post-title { left: 539px; top: 990px; font-size: 16px; font-weight: 400; color: var(--accent); }
  .post-meta { left: 540px; top: 1076px; font-size: 7.5px; color: var(--accent); }
  .post-meta span + span { border-left: 1px solid var(--muted); margin-left: 6px; padding-left: 7px; }

  .footer-links { left: 367px; top: 1171px; font-size: 12.5px; color: var(--white); }
  .footer-links span + span { border-left: 2px solid var(--white); margin-left: 5px; padding-left: 6px; }
  .social { top: 1166px; width: 22px; height: 22px; border-radius: 4px; }
</style>
</head>
<body>

<header class="abs site-header">
  <div class="abs brand"><span class="brand-dot"></span><span class="brand-name">QM Volt</span></div>
  <div class="abs login-field" style="left:608px">Username</div>
  <div class="abs login-field" style="left:704px">Password</div>
  <div class="abs login-links">Login&nbsp; Remember me&nbsp; Sign Up</div>
</header>

<section class="abs hero" role="img" aria-label="Close-up of a glowing circuit board with a small robot figure"></section>
<div class="abs hero-line hero-title">“Technology in your hands”</div>
<div class="abs hero-line hero-sub">Make a life easy</div>

<nav class="abs main-nav">
  <div class="abs nav-item nav-home">HOME</div>
  <div class="abs nav-item" style="left:153px">BLOG</div>
  <div class="abs nav-item" style="left:239px">CONTAC US</div>
  <div class="abs nav-item" style="left:378px">ABOUT US</div>
  <div class="abs nav-item" style="left:499px">NEWS</div>
  <div class="abs nav-item" style="left:577px">SEARCH</div>
  <div class="abs search-box"></div>
  <svg class="abs search-icon" width="24" height="24" viewBox="0 0 24 24" aria-hidden="true">
    <circle cx="10" cy="10" r="7" fill="#e8eef2" stroke="#c9d2d8" stroke-width="2"/>
    <line x1="15" y1="15" x2="21" y2="21" stroke="#9aa4aa" stroke-width="3" stroke-linecap="round"/>
  </svg>
</nav>

<section class="features">
  <h2 class="abs feature-title" style="left:13px;width:233px">Multimedia</h2>
  <h2 class="abs feature-title" style="left:275px;width:233px">Troubleshooting</h2>
  <h2 class="abs feature-title" style="left:533px;width:234px">Hardware</h2>

  <div class="abs" style="left:36px;top:600px;width:224px;height:152px;background:radial-gradient(ellipse 90px 40px at 40% 22%,#7fc0ec,rgba(127,192,236,0) 80%),radial-gradient(ellipse 70px 35px at 75% 40%,#8ccaf0,rgba(140,202,240,0) 80%),linear-gradient(180deg,#ffffff 0%,#eef2f5 55%,#5b6168 72%,#dfe3e6 85%,#ffffff 100%)" role="img" aria-label="Laptop, tablet and phone showing a sky wallpaper"></div>
  <div class="abs" style="left:290px;top:605px;width:204px;height:134px;background:radial-gradient(ellipse 60px 40px at 25% 45%,#6f7880,rgba(111,120,128,0) 80%),radial-gradient(ellipse 80px 30px at 70% 85%,#3c4247,rgba(60,66,71,0) 80%),linear-gradient(160deg,#f3f5f7,#d7dde2 50%,#c3cad0)" role="img" aria-label="Hands repairing a laptop with tools"></div>
  <div class="abs" style="left:548px;top:605px;width:197px;height:129px;background:radial-gradient(circle at 56% 32%,#f0f0f0 0,#c8c9cb 14%,#7e8184 30%,#2a2b2d 55%,#0d0d0d 80%)" role="img" aria-label="Inside of an optical disc drive"></div>

  <p class="abs copy" style="left:13px;width:234px">Lorem Ipsum is simply dummy text of the printing and typesetting industry. Lorem Ipsum has been the industry's standard dummy text ever since the 1500s, when an unknown printer took a galley of type and scrambled it to make a type specimen book. It has survived not only five centuries, but also the leap into electronic typesetting, remaining essentially unchanged. It was popularised in the 1960s with the release of Letraset sheets containing Lorem Ipsum passages,</p>
  <p class="abs copy" style="left:275px;width:234px">Lorem Ipsum is simply dummy text of the printing and typesetting industry. Lorem Ipsum has been the industry's standard dummy text ever since the 1500s, when an unknown printer took a galley of type and scrambled it to make a type specimen book. It has survived not only five centuries, but also the leap into electronic typesetting, remaining essentially unchanged. It was popularised in the 1960s with the release of Letraset sheets containing Lorem Ipsum passages,</p>
  <p class="abs copy" style="left:533px;width:234px">Lorem Ipsum is simply dummy text of the printing and typesetting industry. Lorem Ipsum has been the industry's standard dummy text ever since the 1500s, when an unknown printer took a galley of type and scrambled it to make a type specimen book. It has survived not only five centuries, but also the leap into electronic typesetting, remaining essentially unchanged. It was popularised in the 1960s with the release of Letraset sheets containing Lorem Ipsum passages,</p>

  <div class="abs read-more" style="left:196px">Read More</div>
  <div class="abs read-more" style="left:458px">Read More</div>
  <div class="abs read-more" style="left:716px">Read More</div>
</section>

<section class="abs lower"></section>
<h2 class="abs lower-title" style="left:22px;width:232px;text-align:center">Community</h2>
<h2 class="abs lower-title" style="left:277px;width:233px;text-align:center">e-Commerce</h2>
<h2 class="abs lower-title" style="left:541px">Blog</h2>

<p class="abs copy lower-copy" style="left:22px;top:1012px;width:232px">Lorem Ipsum is simply dummy text of the printing and typesetting industry. Lorem Ipsum has been the industry's standard dummy text ever since the 1500s, when an unknown printer took a galley of type and scrambled it to make a type specimen book. It has survived not only five centuries, but also the leap into electronic typesetting, remaining essentially unchanged. It was popularised in the 1960s with the release of Letraset sheets containing Lore</p>
<p class="abs copy lower-copy" style="left:277px;top:1012px;width:233px">Lorem Ipsum is simply dummy text of the printing and typesetting industry. Lorem Ipsum has been the industry's standard dummy text ever since the 1500s, when an unknown printer took a galley of type and scrambled it to make a type specimen book. It has survived not only five centuries, but also the leap into electronic typesetting, remaining essentially unchanged. It was popularised in the 1960s with the release of Letraset sheets containing Lore</p>

<h3 class="abs post-title">Post Element</h3>
<p class="abs copy lower-copy" style="left:540px;top:1014px;width:235px">Lorem Ipsum is simply dummy text of the printing and typesetting industry. Lorem Ipsum has been the industry's standard dummy text ever since the 1500s, when an unknown printer took a galley of type and scrambled it to make a type</p>
<div class="abs post-meta"><span>No Comment</span><span>Posted December 17<sup>th</sup></span></div>

<footer>
  <div class="abs footer-links"><span>Copyright@2011</span><span>Abous Us</span><span>Contac Us</span><span>Blog</span></div>
  <div class="abs social" style="left:676px;background:#f07a1a"></div>
  <div class="abs social" style="left:704px;background:#f26a12"></div>
  <div class="abs social" style="left:733px;background:#3a5f9e"></div>
  <div class="abs social" style="left:760px;background:#3fb3e6"></div>
</footer>

</body>
</html>
```